Business Card & Logo Design

Originally the brief was for a card only - I now think it's probably better to include a logo design as well. PLease add $200 to the Budget of $210, Apologies for the inconvenience for thaos that have already submitted designs.

Lantern Hollow Productions Pty Ltd is a video/dvd/ production company. Primarily corporate medium to high end. It's a one man operation that's been in business 20 years.

The name " Lantern Hollow" is a primarily a reference to Mathieu Corbelle film that's about film making. Shooting "Lantern Hollow" is also a technique employed by cinematographers to make scenes shot in daylight look like night.

See the design emphasising blue day/night tones but open to other ideas.

Main Text can either be Lantern Hollow Productions or Lantern Hollow.

Many thanks to all designers who submitted ideas for this brief.

Choosing between the designs was very difficult indeed.

I wish everyone the best and may the next job be yours!

Warren

• Text for card:
In Larger Print
Lantern Hollow Productions or Lantern Hollow
Warren Bellamy
In Smaller Print
Lantern Hollow Productions Pty Ltd.
17 Pelham Street
Glen Iris, VIC, 3146
P: 9734 2061
m: 0438 725 190
e: warrenbellamy@ostrafel.com

```html
<!DOCTYPE html>
<html lang="en">
<head>
<meta charset="utf-8">
<title>Lantern Hollow Productions – Business Cards &amp; Logo</title>
<link rel="stylesheet" href="https://fonts.googleapis.com/css2?family=EB+Garamond:wght@500&family=Arimo:wght@700&display=swap">
<style>
  :root {
    --night: #2a2661;
    --day: #b9e3f8;
    --silver: #8f8f8f;
    --paper: #ffffff;
    --ink: #111111;
    --serif: "EB Garamond", Garamond, serif;
    --sans: "Arimo", Arial, sans-serif;
  }
  * { margin: 0; padding: 0; box-sizing: border-box; }
  html, body { width: 1200px; height: 869px; overflow: hidden; background: var(--paper); }
  .sheet { position: relative; width: 1200px; height: 869px; }

  .card { position: absolute; overflow: hidden; box-shadow: 0 0 0 1px rgba(0,0,0,0.06); }

  /* Landscape front card */
  .card--front { left: 60px; top: 40px; width: 591px; height: 386px; }
  .card--front .half { position: absolute; top: 0; bottom: 0; width: 50%; }
  .card--front .half--night { left: 0; background: var(--night); }
  .card--front .half--day { right: 0; background: var(--day); }
  .card--front .emblem { position: absolute; left: 238px; top: -12px; }
  .card--front .wordmark {
    position: absolute; left: 0; right: 0; top: 150px; text-align: center;
    font-family: var(--serif); font-weight: 500; color: var(--paper);
    font-size: 31px; line-height: 32px;
  }
  .card--front .person {
    position: absolute; left: 0; right: 0; top: 232px; text-align: center;
    font-family: var(--sans); font-weight: 700; font-size: 38px; color: var(--silver);
  }
  .card--front .contact {
    position: absolute; top: 344px; font-family: var(--sans); font-weight: 700;
    font-size: 13px; color: var(--paper); white-space: nowrap;
  }
  .contact--phone { left: 24px; }
  .contact--mobile { left: 140px; }
  .contact--email { right: 20px; }

  /* Portrait back card */
  .card--back { left: 731px; top: 48px; width: 405px; height: 633px; background: var(--day); }
  .card--back .band--night { position: absolute; left: 0; top: 0; width: 100%; height: 312px; background: var(--night); }
  .card--back .company {
    position: absolute; left: 0; right: 0; top: 36px; text-align: center;
    font-family: var(--serif); font-weight: 500; font-size: 29px; color: var(--paper);
  }
  .card--back .address {
    position: absolute; left: 0; right: 0; top: 84px; text-align: center;
    font-family: var(--sans); font-weight: 700; font-size: 15px; line-height: 18px; color: var(--paper);
  }
  .card--back .emblem { position: absolute; left: 144px; top: 254px; }
  .card--back .services {
    position: absolute; left: 0; right: 0; top: 434px; list-style: none; text-align: center;
    font-family: var(--sans); font-weight: 700; font-size: 22px; line-height: 27px; color: var(--ink);
  }

  /* Standalone logo */
  .logo { position: absolute; left: 95px; top: 452px; width: 600px; height: 410px; }
  .logo .emblem { position: absolute; left: 185px; top: 0; }
  .logo .name {
    position: absolute; left: 0; right: 0; top: 236px; text-align: center;
    font-family: var(--serif); font-weight: 500; color: var(--night); white-space: nowrap;
  }
  .logo .name-line { display: block; }
  .logo .name-line--main { font-size: 72px; line-height: 78px; }
  .logo .name-line--sub { font-size: 54px; line-height: 62px; letter-spacing: 1px; }
</style>
</head>
<body>
<main class="sheet">

  <section class="card card--front" aria-label="Business card front">
    <div class="half half--night"></div>
    <div class="half half--day"></div>
    <svg class="emblem" width="116" height="116" viewBox="0 0 116 116" aria-hidden="true">
      <circle cx="58" cy="58" r="58" fill="var(--paper)"/>
    </svg>
    <p class="wordmark">Lantern Hollow<br>Productions</p>
    <p class="person">Warren Bellamy</p>
    <p class="contact contact--phone">P: 9734 2061</p>
    <p class="contact contact--mobile">M: 0438 725 190</p>
    <p class="contact contact--email">E: warrenbellamy@ostrafel.com</p>
  </section>

  <section class="card card--back" aria-label="Business card back">
    <div class="band--night"></div>
    <p class="company">Lantern Hollow Productions</p>
    <p class="address">17 Pelham Street<br>Glen Iris, VIC, 3146</p>
    <svg class="emblem" width="116" height="116" viewBox="0 0 116 116" aria-hidden="true">
      <circle cx="58" cy="58" r="58" fill="var(--paper)"/>
    </svg>
    <ul class="services">
      <li>Corporate Video</li>
      <li>Commercial Taping</li>
      <li>Short Film</li>
      <li>Training Film</li>
    </ul>
  </section>

  <section class="logo" aria-label="Lantern Hollow Productions logo">
    <svg class="emblem" width="230" height="230" viewBox="0 0 230 230" aria-hidden="true">
      <circle cx="115" cy="115" r="115" fill="var(--night)"/>
    </svg>
    <p class="name">
      <span class="name-line name-line--main">Lantern Hollow</span>
      <span class="name-line name-line--sub">PRODUCTIONS</span>
    </p>
  </section>

</main>
</body>
</html>
```